Banner Ad Design Project

We need a 728x90 and a 300x250
1st option
"I have a lead for you. Click here to close the deal."
In large bold letters.
Under this in smaller letters,
"Borwelt. For serious business networkers"
2nd option
"Put that coffee down!"
"Coffee's for closers only."
Close more deals. BORWELT LOGO
(this is a quote from Harrowmere Tavish. It is a famous sales movie)
The other option is
"First you get the money" "Then you get the power" in bold letters.
"Borwelt. For serious business networkers" in smaller letters at the bottom.
-Must have our colors
-Must have our logo (Small at the bottom right)
-Watch the video at borwelt () com
Please be creative. If the banner can have multiple images that would be great as well.
This needs to be a serious looking ad that is bold and clean.
Updates
Please be sure to use the phrase, "Put that coffee down! Coffee's for closers only" with the logo and at the bottom the words, Borwelt, for serious business networkers. in one of the designs. This will be our first campaign. I am looking for a very simple design that is bold. Perhaps just a coffee cup with the words and no other graphics.
Target Market(s)
Sales professionals
Industry/Entity Type
Business
Look and feel

```html
<!DOCTYPE html>
<html lang="en">
<head>
<meta charset="utf-8">
<title>Borwelt banner set</title>
<link rel="stylesheet" href="https://fonts.googleapis.com/css2?family=Nanum+Gothic:wght@700;800&display=swap">
<style>
  :root {
    --bg: #4d2613;
    --paper: #ffffff;
    --paper-fade: #f1f3f6;
    --navy: #3a5896;
    --band: #44579c;
    --green: #5a9e2c;
    --green-light: #9ccf36;
    --green-dark: #4f9a18;
    --orange: #f2a51e;
    --rule: #7bb043;
  }
  * { margin: 0; padding: 0; box-sizing: border-box; }
  html, body { width: 1200px; height: 1000px; overflow: hidden; }
  body {
    position: relative;
    background: var(--bg);
    font-family: "Nanum Gothic", Arial, sans-serif;
    font-weight: 800;
    color: var(--navy);
  }
  .ad { position: absolute; background: var(--paper); overflow: hidden; box-shadow: 0 2px 6px rgba(0,0,0,.35); }

  /* 300x250 style square */
  .ad--square { width: 250px; height: 300px; background: linear-gradient(var(--paper) 60%, var(--paper-fade) 84%); }
  .ad--square.one { left: 323px; top: 212px; }
  .ad--square.two { left: 663px; top: 212px; }
  .square__brand { position: absolute; top: 42px; left: 0; right: 0; text-align: center; font-size: 26px; color: var(--navy); }
  .square__brand::before { content: ""; display: inline-block; width: 16px; height: 16px; background: var(--orange); margin-right: 8px; vertical-align: -1px; }
  .square__line { position: absolute; left: 0; right: 0; text-align: center; font-size: 18px; }
  .square__line.lead { top: 120px; }
  .square__line.cta { top: 154px; color: var(--green); }
  .square__line.close { top: 188px; }
  .square__tag { position: absolute; top: 218px; left: 0; right: 0; text-align: center; font-size: 10px; font-weight: 700; }
  .square__foot { position: absolute; left: 0; right: 0; top: 240px; height: 45px; border-top: 3px solid var(--rule); background: var(--paper); }
  .square__foot-brand { position: absolute; left: 14px; top: 12px; font-size: 17px; color: var(--navy); }
  .square__band { position: absolute; left: 0; right: 0; bottom: 0; height: 15px; background: var(--band); }

  .button {
    display: inline-block;
    background: linear-gradient(var(--green-light), var(--green-dark));
    color: #fff;
    border-radius: 2px;
    text-shadow: 0 1px 1px rgba(0,0,0,.25);
  }
  .ad--square .button { width: 142px; height: 24px; line-height: 24px; }

  /* 728x90 leaderboard */
  .ad--wide { width: 728px; height: 90px; left: 261px; border-top: 3px solid var(--rule); background: linear-gradient(var(--paper) 55%, var(--paper-fade)); }
  .ad--wide.one { top: 554px; }
  .ad--wide.two { top: 683px; }
  .wide__brand { position: absolute; left: 8px; top: 22px; font-size: 28px; color: var(--navy); }
  .wide__brand::before { content: ""; display: inline-block; width: 16px; height: 16px; background: var(--orange); margin-right: 8px; vertical-align: 0; }
  .wide__copy { position: absolute; left: 195px; width: 230px; text-align: center; font-size: 18px; }
  .wide__copy.lead { top: 2px; }
  .wide__copy.cta { top: 26px; color: var(--green); }
  .wide__copy.close { top: 50px; }
  .ad--wide .button { width: 142px; height: 24px; line-height: 24px; }
  .wide__tag { position: absolute; left: 424px; top: 58px; font-size: 10px; font-weight: 700; }
  .wide__mark { position: absolute; right: 20px; top: 24px; font-size: 18px; color: var(--navy); }
  .wide__band { position: absolute; left: 0; right: 0; bottom: 0; height: 15px; background: var(--band); border-top: 2px solid #c9d2e2; }
</style>
</head>
<body>

  <section class="ad ad--square one" aria-label="Square banner with button">
    <div class="square__brand">Borwelt</div>
    <p class="square__line lead">I have a lead for you.</p>
    <p class="square__line cta"><span class="button">Click here</span></p>
    <p class="square__line close">to close the deal.</p>
    <p class="square__tag">Borwelt. For serious business networkers</p>
    <div class="square__foot"><span class="square__foot-brand">borwelt</span></div>
    <div class="square__band"></div>
  </section>

  <section class="ad ad--square two" aria-label="Square banner with text link">
    <div class="square__brand">Borwelt</div>
    <p class="square__line lead">I have a lead for you.</p>
    <p class="square__line cta">Click here</p>
    <p class="square__line close">to close the deal.</p>
    <p class="square__tag">Borwelt. For serious business networkers</p>
    <div class="square__foot"><span class="square__foot-brand">borwelt</span></div>
    <div class="square__band"></div>
  </section>

  <section class="ad ad--wide one" aria-label="Leaderboard banner with button">
    <div class="wide__brand">borwelt</div>
    <p class="wide__copy lead">I have a lead for you.</p>
    <p class="wide__copy cta"><span class="button">Click here</span></p>
    <p class="wide__copy close">to close the deal.</p>
    <p class="wide__tag">Borwelt. For serious business networkers</p>
    <div class="wide__mark">Borwelt</div>
    <div class="wide__band"></div>
  </section>

  <section class="ad ad--wide two" aria-label="Leaderboard banner with text link">
    <div class="wide__brand">borwelt</div>
    <p class="wide__copy lead">I have a lead for you.</p>
    <p class="wide__copy cta">Click here</p>
    <p class="wide__copy close">to close the deal.</p>
    <p class="wide__tag">Borwelt. For serious business networkers</p>
    <div class="wide__mark">Borwelt</div>
    <div class="wide__band"></div>
  </section>

</body>
</html>
```